Glass window Vinyl

We are in need of window vinyls for the building shown in the photos. The current vinyls will come down, and we will install the new signage created by this process. We need to advertise:

"Hartwell's Landing Pop Up Market"

Then, below that, it should say for rental inquiries call : 717.555.0193 with our logo which is attached along with our colors and brand guidelines. You may add more color to the Hartwells landing pop up market signage if appropriate. It should be large enough to be easily read from the road by those passing by.

```html
<!DOCTYPE html>
<html lang="en">
<head>
<meta charset="utf-8">
<title>Hartwell's Landing Pop Up Market – Window Vinyl Options</title>
<link href="https://fonts.googleapis.com/css2?family=Bebas+Neue&family=Montserrat:wght@500;700;800&display=swap" rel="stylesheet">
<style>
  :root {
    --backdrop: #666666;
    --teal-deep: #0f4a5a;
    --teal-mid: #1b6a78;
    --teal-glow: #2b8d95;
    --navy-shade: #263a52;
    --charcoal: #3c3c3a;
    --gold: #c2a86a;
    --sage: #c5d0c6;
    --white: #ffffff;
    --cream: #fdf8c4;
    --brand-ink: #123f4d;
  }
  * { margin: 0; padding: 0; box-sizing: border-box; }
  html, body { width: 1200px; height: 1200px; overflow: hidden; }
  body { background: var(--backdrop); position: relative; font-family: "Montserrat", sans-serif; }

  .sign {
    position: absolute;
    width: 814px; height: 814px;
    transform: scale(0.6204);
    transform-origin: top left;
    overflow: hidden;
    box-shadow: 0 6px 14px rgba(0,0,0,0.25);
  }
  .sign--brand-top { left: 77px; top: 348px; }
  .sign--brand-bottom { left: 617px; top: 346px; }
  .sign__art { position: absolute; inset: 0; width: 814px; height: 814px; }

  .sign__text { position: absolute; left: 0; width: 814px; text-align: center; }

  .headline {
    font-family: "Bebas Neue", sans-serif;
    font-size: 112px;
    line-height: 100px;
    letter-spacing: 0;
  }
  .sign--brand-top .headline { top: 334px; color: var(--cream); text-shadow: 0 3px 6px rgba(0,0,0,0.25); }
  .sign--brand-bottom .headline { top: 62px; color: var(--white); text-shadow: 0 3px 6px rgba(0,0,0,0.3); }

  .inquiry { font-weight: 700; color: var(--white); }
  .sign--brand-top .inquiry { top: 590px; font-size: 43px; text-transform: uppercase; letter-spacing: 0.5px; }
  .sign--brand-bottom .inquiry { top: 325px; font-size: 44px; }
  .inquiry-rule {
    position: absolute; left: 126px; top: 385px;
    width: 563px; height: 4px; background: var(--sage);
  }

  .phone { font-weight: 800; font-size: 84px; line-height: 1; letter-spacing: 1px; }
  .sign--brand-top .phone { top: 658px; color: var(--cream); }
  .sign--brand-bottom .phone { top: 398px; color: var(--white); text-shadow: 0 3px 6px rgba(0,0,0,0.25); }

  .brand { position: absolute; left: 0; width: 814px; text-align: center; color: var(--brand-ink); font-weight: 500; }
  .sign--brand-top .brand { top: 60px; }
  .sign--brand-bottom .brand { top: 582px; }
  .brand__mark {
    display: block; margin: 0 auto 28px;
    width: 38px; height: 38px;
    border: 4px solid var(--gold);
  }
  .brand__name { display: block; font-size: 44px; letter-spacing: 12px; line-height: 1; }
  .brand__tagline { display: block; margin-top: 26px; font-size: 17px; letter-spacing: 9px; line-height: 1; }
</style>
</head>
<body>

  <section class="sign sign--brand-top" aria-label="Window vinyl option with brand at top">
    <svg class="sign__art" viewBox="0 0 814 814" aria-hidden="true">
      <defs>
        <linearGradient id="tealTop" x1="0" y1="0" x2="1" y2="1">
          <stop offset="0" stop-color="#0f4a5a"/>
          <stop offset="0.5" stop-color="#1b6a78"/>
          <stop offset="1" stop-color="#263a52"/>
        </linearGradient>
      </defs>
      <rect width="814" height="814" fill="url(#tealTop)"/>
      <path d="M0 720 Q500 700 814 230 L814 814 L0 814 Z" fill="#0f4a5a" opacity="0.45"/>
      <path d="M640 814 Q760 740 814 690 L814 814 Z" fill="#0f4a5a"/>
      <rect width="814" height="70" fill="var(--charcoal)"/>
      <path d="M0 46 Q420 -10 814 40 L814 60 L0 60 Z" fill="var(--gold)"/>
      <path d="M0 240 Q420 290 814 232 L814 260 Q420 290 0 250 Z" fill="var(--sage)"/>
      <path d="M0 56 Q420 2 814 44 L814 230 Q420 290 0 232 Z" fill="var(--white)"/>
    </svg>

    <div class="brand">
      <span class="brand__mark"></span>
      <span class="brand__name">BIRCHWOOD ROW</span>
      <span class="brand__tagline">PROPERTIES</span>
    </div>

    <h1 class="sign__text headline">Hartwell's Landing<br>Pop Up Market</h1>
    <p class="sign__text inquiry">For Rental Inquiries Call</p>
    <p class="sign__text phone">717 555 0193</p>
  </section>

  <section class="sign sign--brand-bottom" aria-label="Window vinyl option with brand at bottom">
    <svg class="sign__art" viewBox="0 0 814 814" aria-hidden="true">
      <defs>
        <radialGradient id="tealGlow" cx="0.2" cy="0.68" r="0.7">
          <stop offset="0" stop-color="#2b8d95"/>
          <stop offset="0.45" stop-color="#1b6a78"/>
          <stop offset="1" stop-color="#0f4a5a"/>
        </radialGradient>
      </defs>
      <rect width="814" height="814" fill="url(#tealGlow)"/>
      <path d="M330 0 L420 0 L0 330 L0 260 Z" fill="#0f4a5a" opacity="0.35"/>
      <path d="M560 0 L650 0 L140 560 L80 560 Z" fill="#0f4a5a" opacity="0.3"/>
      <path d="M814 330 L814 420 L560 560 L480 560 Z" fill="#0f4a5a" opacity="0.3"/>
      <rect y="760" width="814" height="54" fill="var(--charcoal)"/>
      <path d="M0 562 Q420 510 814 578 L814 780 Q420 815 0 760 Z" fill="var(--gold)"/>
      <path d="M0 570 Q420 520 814 588 L814 768 Q420 800 0 750 Z" fill="var(--white)"/>
    </svg>

    <h2 class="sign__text headline">Hartwell's Landing<br>Pop Up Market</h2>
    <p class="sign__text inquiry">For Rental Inquiries Call</p>
    <span class="inquiry-rule" aria-hidden="true"></span>
    <p class="sign__text phone">717 555 0193</p>

    <div class="brand">
      <span class="brand__mark"></span>
      <span class="brand__name">BIRCHWOOD ROW</span>
      <span class="brand__tagline">PROPERTIES</span>
    </div>
  </section>

</body>
</html>
```